Business card design to suit our website

Need a nice looking business card for our business based off images from our Website and provided images. The business card will require 2 different names (for the 2 owners). The business card should include images from our website, facebook (keel bracket works set) or the pictures provided. it should also contain all contact information.
Our website is www.keelbracketworks.com.au
Please dont use image from top bar of website. If images are used please use the ones of our product under the buy it now tab

Target Market(s)

Automotive

Industry/Entity Type

Automotive Part

Contact Information for Business Card

Business Name. contact details including names phone number email. logo
2 business cards needed with 2 different persons names and phone number.

Colors

Designer to choose colors to be used in the design.

Requirements
Must have
• whatever looks best

```html
<!DOCTYPE html>
<html lang="en">
<head>
<meta charset="utf-8">
<title>Steadfast Business Card</title>
<link href="https://fonts.googleapis.com/css2?family=Roboto:wght@400;500;700;900&display=swap" rel="stylesheet">
<style>
  :root {
    --page-bg: #e9e6e2;
    --card-white: #f4f4f4;
    --card-dark: #1b1e27;
    --brand-red: #c0202e;
    --ink: #1a1a1a;
    --ink-soft: #4a4a4a;
    --divider: #cfcfcf;
    --white: #ffffff;
  }
  * { box-sizing: border-box; margin: 0; padding: 0; }
  html, body {
    width: 1200px; height: 960px; overflow: hidden;
    background: var(--page-bg);
    font-family: "Roboto", Arial, sans-serif;
  }
  .canvas { position: relative; width: 1200px; height: 960px; }

  .card {
    position: absolute; width: 600px; height: 342px;
    border-radius: 18px; overflow: hidden;
  }
  .card--front { left: 302px; top: 125px; background: var(--card-white); }
  .card--back { left: 299px; top: 493px; background: var(--card-dark); }

  /* front */
  .brand-block {
    position: absolute; left: 38px; top: 128px; width: 232px;
    text-align: center;
  }
  .brand-name {
    display: flex; align-items: center; justify-content: center; gap: 8px;
    font-weight: 900; font-size: 38px; color: var(--brand-red); line-height: 1;
  }
  .brand-dot { width: 14px; height: 14px; border-radius: 50%; background: var(--brand-red); }
  .brand-tagline {
    margin-top: 12px; font-weight: 700; font-size: 18px; color: var(--ink-soft);
  }
  .divider {
    position: absolute; left: 291px; top: 113px; width: 1px; height: 113px;
    background: var(--divider);
  }
  .contact-block { position: absolute; left: 316px; top: 113px; }
  .person-name { font-size: 23px; font-weight: 500; color: var(--brand-red); line-height: 1; }
  .person-role { margin-top: 4px; font-size: 14px; font-weight: 500; color: var(--ink); }
  .contact-list { list-style: none; margin-top: 14px; }
  .contact-item {
    display: flex; align-items: center; gap: 8px;
    font-size: 14px; color: var(--ink-soft); line-height: 19px;
  }
  .contact-icon { width: 13px; height: 13px; fill: var(--brand-red); flex: none; }
  .edge-band { position: absolute; left: 0; bottom: 0; width: 600px; height: 17px; }

  /* back */
  .track-band {
    position: absolute; left: 0; width: 600px; background: var(--brand-red);
  }
  .track-band--upper { top: 134px; height: 37px; }
  .track-band--lower { top: 185px; height: 38px; }
  .back-brand {
    position: absolute; left: 0; width: 600px; text-align: center;
  }
  .back-brand__name {
    top: 110px; display: flex; justify-content: center; align-items: center; gap: 10px;
    font-weight: 900; font-size: 52px; color: var(--white); line-height: 1;
  }
  .back-brand__dot { width: 18px; height: 18px; border-radius: 50%; background: var(--white); }
  .back-brand__tagline {
    top: 188px; font-weight: 700; font-size: 27px; color: var(--white); line-height: 32px;
  }
</style>
</head>
<body>
<main class="canvas">

  <section class="card card--front">
    <div class="brand-block">
      <div class="brand-name"><span class="brand-dot"></span>Steadfast</div>
      <div class="brand-tagline">Bracket Works Set</div>
    </div>
    <div class="divider"></div>
    <div class="contact-block">
      <p class="person-name">DANIEL HART</p>
      <p class="person-role">CEO/FOUNDER</p>
      <ul class="contact-list">
        <li class="contact-item">
          <svg class="contact-icon" viewBox="0 0 24 24"><path d="M6.6 10.8a15 15 0 0 0 6.6 6.6l2.2-2.2a1 1 0 0 1 1-.25 11.4 11.4 0 0 0 3.6.57 1 1 0 0 1 1 1V20a1 1 0 0 1-1 1A17 17 0 0 1 3 4a1 1 0 0 1 1-1h3.5a1 1 0 0 1 1 1c0 1.25.2 2.45.57 3.57a1 1 0 0 1-.25 1z"/></svg>
          1300 482 117
        </li>
        <li class="contact-item">
          <svg class="contact-icon" viewBox="0 0 24 24"><path d="M2 5h20v14H2z M2 5l10 8 10-8" fill="none" stroke="#c0202e" stroke-width="0"/><path d="M2 5h20v2l-10 7L2 7z"/><path d="M2 9l10 7 10-7v10H2z"/></svg>
          daniel@keelbracketworks.com.au
        </li>
        <li class="contact-item">
          <svg class="contact-icon" viewBox="0 0 24 24"><circle cx="12" cy="12" r="10"/><path d="M2 12h20M12 2c3 3 3 17 0 20M12 2c-3 3-3 17 0 20" fill="none" stroke="#f4f4f4" stroke-width="1.5"/></svg>
          www.keelbracketworks.com.au
        </li>
      </ul>
    </div>
    <svg class="edge-band" viewBox="0 0 600 17" preserveAspectRatio="none">
      <polygon points="0,0 392,0 387,17 0,17" fill="#c0202e"/>
      <polygon points="396,0 600,0 600,17 391,17" fill="#000000"/>
    </svg>
  </section>

  <section class="card card--back">
    <div class="track-band track-band--upper" role="img" aria-label="Red band with tyre tread pattern"></div>
    <div class="track-band track-band--lower" role="img" aria-label="Red band with tyre tread pattern"></div>
    <div class="back-brand back-brand__name"><span class="back-brand__dot"></span>Steadfast</div>
    <div class="back-brand back-brand__tagline">Bracket Works Set</div>
  </section>

</main>
</body>
</html>
```